Admin Backend Redesign

We need a redesign for our backend which supoosed to make the backoffice look more modern!

I will add screenshots of the backoffice so you know what data will be shown in the Admin.

Have in mind that the users of this backend are Doctors. We need a clinical look, modern and sharp. The backoffice is responsive, have that in mind. We need the backoffice to look as professional as possible.

The theme used for the website is: http://velmora.quillstack-sample.com/

ON the main page of the backoffice, under every widget i need some space to write an explanation what the widget is about.

The color code used in our logo and website is #57aad4 combined with white.

We are open for ideas!
Updates

Project Deadline Extended
Reason: Designs are ok, but nothing innovative. Please use more modern designs!

Project Deadline Extended
Reason: Havent recieved a perfect design yet. Please read instructions carefully! Thank you

Project Deadline Extended
Reason: Hey everybody, sorry for the delay. We will decide in 3 days. If anyone wants to add a Design, that would be great.

Target Market(s)

Doctors, therapists

Industry/Entity Type

It Professional

Font styles to use
Sans Serif

Requirements
Must have
• Must look uptodate, modern, like new back offices look nowadays

```html
<!DOCTYPE html>
<html lang="en">
<head>
<meta charset="utf-8">
<title>Users Accounts – Admin</title>
<link rel="stylesheet" href="https://fonts.googleapis.com/css2?family=Open+Sans:wght@400;600;700&display=swap">
<style>
  :root{
    --brand:#57aad4;
    --brand-mid:#3d8dbb;
    --brand-dark:#2b7ca8;
    --brand-deep:#1c6a97;
    --footer:#135a80;
    --head-grey:#a6aeb8;
    --row-alt:#f6f6f6;
    --text:#333;
    --muted:#9a9a9a;
    --icon:#8a8a8a;
    --accent:#ec4e5f;
    --star:#f8c23a;
    --ok:#2ca84a;
    --bad:#e0202a;
    --white:#fff;
  }
  *{box-sizing:border-box;margin:0;padding:0}
  html,body{width:1200px;height:1125px;overflow:hidden;background:var(--white);font-family:"Open Sans",Arial,sans-serif;color:var(--text)}
  .canvas{position:relative;width:1200px;height:1125px}
  .topbar{position:absolute;left:0;top:0;width:1200px;height:45px;background:var(--brand);color:var(--white)}
  .brand-name{position:absolute;left:105px;top:7px;font-size:22px;font-weight:400;letter-spacing:-.5px}
  .user{position:absolute;left:887px;top:11px;font-size:19px;display:flex;align-items:center;gap:12px}
  .topbar .divider{position:absolute;left:1042px;top:0;width:1px;height:45px;background:rgba(255,255,255,.35)}
  .topbar .gear{position:absolute;left:1054px;top:12px}
  .sidebar{position:absolute;left:105px;top:66px;width:216px;height:303px;background:var(--brand-mid);border-radius:4px}
  .sidebar:before{content:"";position:absolute;left:28px;top:-10px;border:9px solid transparent;border-top:0;border-bottom:10px solid var(--brand-mid)}
  .menu-toggle{position:absolute;left:171px;top:8px;width:36px;height:27px;background:var(--brand-deep);border-radius:3px;display:flex;flex-direction:column;justify-content:center;align-items:center;gap:3px}
  .menu-toggle span{width:15px;height:2px;background:var(--white)}
  .nav-item{position:absolute;left:0;width:216px;height:40px;display:flex;align-items:center;gap:12px;padding-left:10px;font-size:15.5px;color:var(--white)}
  .nav-item.first{top:44px}
  .nav-item.second{top:85px;border-top:1px solid rgba(255,255,255,.25)}
  .nav-item.active{top:131px;left:-1px;width:217px;background:var(--white);color:#777;padding-left:17px}
  .crumbs{position:absolute;left:352px;top:67px;width:737px;height:39px;background:#f5f5f5;border-radius:5px;display:flex;align-items:center;gap:8px;padding-left:16px;font-size:13px;color:#444}
  .panel-title{position:absolute;left:352px;top:133px;width:737px;height:54px;background:var(--brand-dark);border-bottom:3px solid #4a93bd;border-radius:4px 4px 0 0;color:var(--white);font-weight:700;font-size:16px;padding:18px 0 0 18px}
  .btn{position:absolute;height:42px;border-radius:3px;overflow:hidden;display:flex;color:var(--white);font-size:16px}
  .btn .label{background:var(--brand-mid);display:flex;align-items:center;padding:0 8px}
  .btn .cap{background:var(--brand-deep);display:flex;align-items:center;justify-content:center}
  .btn.add{left:350px;top:204px;width:183px}
  .btn.add .label{width:131px}.btn.add .cap{width:52px}
  .btn.tools{left:951px;top:204px;width:136px}
  .btn.tools .label{width:84px;gap:10px;padding-left:9px}.btn.tools .cap{width:52px}
  .page-size{position:absolute;left:350px;top:259px;width:58px;height:24px;border:2px solid #ddd;font-size:12px;padding:3px 0 0 9px}
  .page-size:after{content:"";position:absolute;right:6px;top:9px;border:4px solid transparent;border-top:5px solid #ccc}
  .search{position:absolute;left:881px;top:255px;width:208px;height:33px;border:2px solid #e2e2e2;border-radius:2px;font-size:11px;color:#999;padding:8px 0 0 7px}
  table.users{position:absolute;left:352px;top:300px;width:737px;border-collapse:collapse;border-bottom:3px solid #e6e6e6}
  .users th{height:32px;background:var(--head-grey);color:var(--white);font-size:12.5px;font-weight:700;text-align:left}
  .users td{height:48.7px;font-size:12px;color:var(--muted);vertical-align:middle}
  .users tbody tr:nth-child(even){background:var(--row-alt)}
  .box{display:inline-block;width:16px;height:16px;border:2px solid #888;border-radius:3px;vertical-align:middle;position:relative}
  th .box{border-color:#fff;background:#fff}
  .player{display:flex;align-items:center;gap:8px}
  .track{position:relative;width:72px;height:5px;background:#e2e2e2;border-radius:2px}
  .track:before{content:"";position:absolute;left:0;top:0;width:31px;height:5px;background:var(--accent);border-radius:2px}
  .track span{position:absolute;left:2px;top:-12px;font-size:7px;color:#999}
  .info{position:absolute;left:352px;top:612px;font-size:11.5px;color:#333}
  .pager{position:absolute;left:837px;top:613px;width:255px;height:33px;display:flex;border-radius:3px;overflow:hidden}
  .pager span{flex:1;background:var(--brand-deep);color:var(--white);font-size:11px;font-weight:700;display:flex;align-items:center;justify-content:center;border-left:1px solid rgba(255,255,255,.2)}
  .pager span.current{background:#0f4f73}
  .pager span.edge{flex:1.05;background:#1a6494}
  .footer{position:absolute;left:0;top:1090px;width:1200px;height:35px;background:var(--footer)}
</style>
</head>
<body>
<div class="canvas">
  <header class="topbar">
    <div class="brand-name">Logo here</div>
    <div class="user">
      <svg width="16" height="17" viewBox="0 0 16 17"><circle cx="8" cy="4.5" r="4" fill="#fff"/><path d="M0 17c0-5 3.5-7 8-7s8 2 8 7z" fill="#fff"/></svg>
      Dr. Mara Lenk
    </div>
    <div class="divider"></div>
    <svg class="gear" width="21" height="21" viewBox="0 0 24 24"><path fill="#fff" d="M19.4 13a7.5 7.5 0 0 0 0-2l2.1-1.6-2-3.5-2.5 1a7.6 7.6 0 0 0-1.7-1L15 3h-4l-.4 2.9a7.6 7.6 0 0 0-1.7 1l-2.5-1-2 3.5L6.5 11a7.5 7.5 0 0 0 0 2l-2.1 1.6 2 3.5 2.5-1a7.6 7.6 0 0 0 1.7 1L11 21h4l.4-2.9a7.6 7.6 0 0 0 1.7-1l2.5 1 2-3.5zM13 15.5a3.5 3.5 0 1 1 0-7 3.5 3.5 0 0 1 0 7z"/></svg>
  </header>

  <aside class="sidebar">
    <div class="menu-toggle"><span></span><span></span><span></span></div>
    <div class="nav-item first">
      <svg width="18" height="16" viewBox="0 0 18 16"><path fill="#fff" d="M9 0 0 8h2.5v8h4.5v-5h4v5h4.5V8H18z"/></svg>Dashboard
    </div>
    <div class="nav-item second">
      <svg width="16" height="17" viewBox="0 0 16 17"><circle cx="8" cy="4.5" r="4" fill="#fff"/><path d="M0 17c0-5 3.5-7 8-7s8 2 8 7z" fill="#fff"/></svg>Pnteger ornare libero
    </div>
    <div class="nav-item active">
      <svg width="16" height="17" viewBox="0 0 16 17"><circle cx="8" cy="4.5" r="4" fill="#bbb"/><path d="M0 17c0-5 3.5-7 8-7s8 2 8 7z" fill="#bbb"/></svg>Lorem ipsum libero
    </div>
  </aside>

  <nav class="crumbs">
    <svg width="15" height="13" viewBox="0 0 18 16"><path fill="#aaa" d="M9 0 0 8h2.5v8h4.5v-5h4v5h4.5V8H18z"/></svg>
    <span>Dashboard</span>
    <svg width="7" height="10" viewBox="0 0 7 10"><path d="M1 1l4 4-4 4" stroke="#777" fill="none"/></svg>
    <span>Inner page2</span>
  </nav>

  <div class="panel-title">Users Accounts</div>

  <div class="btn add">
    <div class="label">Add lorem ipsum</div>
    <div class="cap"><svg width="16" height="16" viewBox="0 0 16 16"><path fill="#fff" d="M6 0h4v6h6v4h-6v6H6v-6H0V6h6z"/></svg></div>
  </div>
  <div class="btn tools">
    <div class="label"><svg width="12" height="8" viewBox="0 0 12 8"><path fill="#fff" d="M0 0h12L6 8z"/></svg>Tools</div>
    <div class="cap"><svg width="21" height="21" viewBox="0 0 24 24"><path fill="#fff" d="M19.4 13a7.5 7.5 0 0 0 0-2l2.1-1.6-2-3.5-2.5 1a7.6 7.6 0 0 0-1.7-1L15 3h-4l-.4 2.9a7.6 7.6 0 0 0-1.7 1l-2.5-1-2 3.5L6.5 11a7.5 7.5 0 0 0 0 2l-2.1 1.6 2 3.5 2.5-1a7.6 7.6 0 0 0 1.7 1L11 21h4l.4-2.9a7.6 7.6 0 0 0 1.7-1l2.5 1 2-3.5zM13 15.5a3.5 3.5 0 1 1 0-7 3.5 3.5 0 0 1 0 7z"/></svg></div>
  </div>

  <div class="page-size">10</div>
  <div class="search">Search</div>

  <svg width="0" height="0" style="position:absolute">
    <defs>
      <path id="star" d="M6 0l1.8 3.9 4.2.4-3.2 2.8 1 4.1L6 9.1 2.2 11.2l1-4.1L0 4.3l4.2-.4z"/>
      <g id="check"><path d="M3 8l3 3 6-8" stroke="#777" stroke-width="1.6" fill="none"/></g>
      <g id="pencil"><path d="M3 15l1-4 9-9 3 3-9 9zM11 4l3 3M4 11l3 3" stroke="#888" stroke-width="1.2" fill="none"/></g>
      <g id="trash"><path d="M2 4h14M7 4V2h4v2M4 4l1 13h8l1-13M7 7v8M9 7v8M11 7v8" stroke="#888" stroke-width="1.2" fill="none"/></g>
      <g id="play">
        <path d="M6 5L1 8l5 3zM11 5L6 8l5 3z" fill="#ccc"/>
        <circle cx="29" cy="8" r="8" fill="#ec4e5f"/><path d="M26.5 4.5v7l6-3.5z" fill="#fff"/>
        <path d="M47 5l5 3-5 3zM52 5l5 3-5 3z" fill="#ccc"/>
      </g>
    </defs>
  </svg>

  <table class="users">
    <colgroup><col style="width:53px"><col style="width:100px"><col style="width:110px"><col style="width:99px"><col style="width:183px"><col style="width:82px"><col style="width:61px"><col></colgroup>
    <thead>
      <tr><th style="padding-left:19px"><span class="box"></span></th><th>Name</th><th>Tell</th><th>Created</th><th>Created</th><th>Last Login</th><th>Status</th><th>Status</th></tr>
    </thead>
    <tbody>
      <tr>
        <td style="padding-left:19px"><span class="box"><svg width="14" height="14" viewBox="0 0 14 14" style="position:absolute;left:-1px;top:-1px"><use href="#check"/></svg></span></td>
        <td>Class aptent</td><td>90418263704</td>
        <td><svg width="68" height="12" viewBox="0 0 68 12"><use href="#star" fill="#f8c23a"/><use href="#star" x="14" fill="#f8c23a"/><use href="#star" x="28" fill="#f8c23a"/><use href="#star" x="42" fill="#f8c23a"/><use href="#star" x="56" fill="#f8c23a"/></svg></td>
        <td><div class="player"><svg width="60" height="16"><use href="#play"/></svg><div class="track"><span>20:30</span></div><svg width="14" height="11" viewBox="0 0 14 11"><path d="M0 3h3l4-3v11L3 8H0z" fill="#bbb"/><path d="M9 3a3 3 0 0 1 0 5M11 1a6 6 0 0 1 0 9" stroke="#bbb" fill="none"/></svg></div></td>
        <td style="padding-left:20px"><svg width="18" height="18"><use href="#pencil"/></svg></td>
        <td style="padding-left:16px"><svg width="18" height="19"><use href="#trash"/></svg></td>
        <td style="padding-left:14px"><svg width="12" height="10" viewBox="0 0 12 10"><path d="M1 5l3 3 7-7" stroke="#2ca84a" stroke-width="1.5" fill="none"/></svg></td>
      </tr>
      <tr>
        <td style="padding-left:19px"><span class="box"></span></td>
        <td>Class aptent</td><td>90418263704</td>
        <td><svg width="68" height="12" viewBox="0 0 68 12"><use href="#star" fill="#f8c23a"/><use href="#star" x="14" fill="#f8c23a"/><use href="#star" x="28" fill="#f8c23a"/><use href="#star" x="42" fill="#f8c23a"/><use href="#star" x="56" fill="#aaa"/></svg></td>
        <td><div class="player"><svg width="60" height="16"><use href="#play"/></svg><div class="track"><span>20:30</span></div><svg width="14" height="11" viewBox="0 0 14 11"><path d="M0 3h3l4-3v11L3 8H0z" fill="#bbb"/><path d="M9 3a3 3 0 0 1 0 5M11 1a6 6 0 0 1 0 9" stroke="#bbb" fill="none"/></svg></div></td>
        <td style="padding-left:20px"><svg width="18" height="18"><use href="#pencil"/></svg></td>
        <td style="padding-left:16px"><svg width="18" height="19"><use href="#trash"/></svg></td>
        <td style="padding-left:14px"><svg width="12" height="10" viewBox="0 0 12 10"><path d="M1 5l3 3 7-7" stroke="#2ca84a" stroke-width="1.5" fill="none"/></svg></td>
      </tr>
      <tr>
        <td style="padding-left:19px"><span class="box"><svg width="14" height="14" viewBox="0 0 14 14" style="position:absolute;left:-1px;top:-1px"><use href="#check"/></svg></span></td>
        <td>Class aptent</td><td>90418263704</td>
        <td><svg width="68" height="12" viewBox="0 0 68 12"><use href="#star" fill="#f8c23a"/><use href="#star" x="14" fill="#f8c23a"/><use href="#star" x="28" fill="#f8c23a"/><use href="#star" x="42" fill="#f8c23a"/><use href="#star" x="56" fill="#aaa"/></svg></td>
        <td><div class="player"><svg width="60" height="16"><use href="#play"/></svg><div class="track"><span>20:30</span></div><svg width="14" height="11" viewBox="0 0 14 11"><path d="M0 3h3l4-3v11L3 8H0z" fill="#bbb"/><path d="M9 3a3 3 0 0 1 0 5M11 1a6 6 0 0 1 0 9" stroke="#bbb" fill="none"/></svg></div></td>
        <td style="padding-left:20px"><svg width="18" height="18"><use href="#pencil"/></svg></td>
        <td style="padding-left:16px"><svg width="18" height="19"><use href="#trash"/></svg></td>
        <td style="padding-left:14px"><svg width="12" height="10" viewBox="0 0 12 10"><path d="M1 5l3 3 7-7" stroke="#2ca84a" stroke-width="1.5" fill="none"/></svg></td>
      </tr>
      <tr>
        <td style="padding-left:19px"><span class="box"></span></td>
        <td>Class aptent</td><td>90418263704</td>
        <td><svg width="68" height="12" viewBox="0 0 68 12"><use href="#star" fill="#f8c23a"/><use href="#star" x="14" fill="#f8c23a"/><use href="#star" x="28" fill="#f8c23a"/><use href="#star" x="42" fill="#f8c23a"/><use href="#star" x="56" fill="#aaa"/></svg></td>
        <td><div class="player"><svg width="60" height="16"><use href="#play"/></svg><div class="track"><span>20:30</span></div><svg width="14" height="11" viewBox="0 0 14 11"><path d="M0 3h3l4-3v11L3 8H0z" fill="#bbb"/><path d="M9 3a3 3 0 0 1 0 5M11 1a6 6 0 0 1 0 9" stroke="#bbb" fill="none"/></svg></div></td>
        <td style="padding-left:20px"><svg width="18" height="18"><use href="#pencil"/></svg></td>
        <td style="padding-left:16px"><svg width="18" height="19"><use href="#trash"/></svg></td>
        <td style="padding-left:14px"><svg width="12" height="10" viewBox="0 0 12 10"><path d="M1 5l3 3 7-7" stroke="#e0202a" stroke-width="1.5" fill="none"/></svg></td>
      </tr>
      <tr>
        <td style="padding-left:19px"><span class="box"><svg width="14" height="14" viewBox="0 0 14 14" style="position:absolute;left:-1px;top:-1px"><use href="#check"/></svg></span></td>
        <td>Class aptent</td><td>90418263704</td>
        <td><svg width="68" height="12" viewBox="0 0 68 12"><use href="#star" fill="#f8c23a"/><use href="#star" x="14" fill="#f8c23a"/><use href="#star" x="28" fill="#f8c23a"/><use href="#star" x="42" fill="#f8c23a"/><use href="#star" x="56" fill="#aaa"/></svg></td>
        <td><div class="player"><svg width="60" height="16"><use href="#play"/></svg><div class="track"><span>20:30</span></div><svg width="14" height="11" viewBox="0 0 14 11"><path d="M0 3h3l4-3v11L3 8H0z" fill="#bbb"/><path d="M9 3a3 3 0 0 1 0 5M11 1a6 6 0 0 1 0 9" stroke="#bbb" fill="none"/></svg></div></td>
        <td style="padding-left:20px"><svg width="18" height="18"><use href="#pencil"/></svg></td>
        <td style="padding-left:16px"><svg width="18" height="19"><use href="#trash"/></svg></td>
        <td style="padding-left:14px"><svg width="12" height="10" viewBox="0 0 12 10"><path d="M1 5l3 3 7-7" stroke="#e0202a" stroke-width="1.5" fill="none"/></svg></td>
      </tr>
    </tbody>
  </table>

  <div class="info">Showing 1 to 5 of 50 entries</div>
  <div class="pager">
    <span class="edge"><svg width="8" height="10" viewBox="0 0 8 10"><path d="M6 1L2 5l4 4" stroke="#fff" stroke-width="2" fill="none"/></svg></span>
    <span>1</span><span class="current">2</span><span>3</span><span>4</span><span>5</span>
    <span class="edge"><svg width="8" height="10" viewBox="0 0 8 10"><path d="M2 1l4 4-4 4" stroke="#fff" stroke-width="2" fill="none"/></svg></span>
  </div>

  <footer class="footer"></footer>
</div>
</body>
</html>
```